Redesign website for small print company

Vindaborgprent is a small printing company in Iceland mainly servicing Students, schools, etc. We are also doing all kind of other jobs, like business cards, book printing, brochure printing etc. We are also selling books online.
Our website is: www.vindaborgprent.is
What we are looking for is:
- Web Design (Uncoded - PSD layout only)
- Mobile friendly design, using our current color scheme: Red, green, yellow and light gray.
- Clean simple design
- Simple, light and easy to use.
- More menu Items/drop down
Industry/Entity Type
Digital Printing
Number of Pages Required
5+ page
Requirements
Must have
- Easy navigation
- Designed for mobile
- Current color scheme (see logo)
Nice to have
- Icon based products

```html
<!DOCTYPE html>
<html lang="en">
<head>
<meta charset="utf-8">
<title>Vindaborgprent</title>
<link rel="stylesheet" href="https://fonts.googleapis.com/css2?family=Roboto:wght@400;500;700&display=swap">
<style>
:root{
  --red:#e21b23;
  --red-dark:#c8141b;
  --yellow:#f7e21b;
  --orange:#f39a1e;
  --green:#1d5a2c;
  --green-dark:#174a24;
  --gray:#f4f4f4;
  --line:#d9d9d9;
  --text:#222;
  --muted:#444;
}
*{box-sizing:border-box;margin:0;padding:0}
html,body{width:1200px;height:3666px;overflow:hidden}
body{position:relative;font-family:"Roboto",Arial,sans-serif;color:var(--text);background:#fff}
.abs{position:absolute}
/* top bar */
.topbar{left:0;top:0;width:1200px;height:30px;background:var(--red);color:#fff;font-size:11px}
.topbar .lang{left:163px;top:9px;display:flex;gap:6px}
.topbar .lang span{width:16px;height:11px;background:#fff;opacity:.85;display:block}
.topbar .lang span+span{background:#2b4aa0}
.topbar .contact{right:165px;top:8px;display:flex;gap:26px}
/* header */
.header{left:0;top:30px;width:1200px;height:95px;background:#fff}
.brand{left:160px;top:28px;display:flex;align-items:center;gap:10px}
.brand .mark{width:30px;height:30px;background:var(--red)}
.brand .name{font-size:24px;font-weight:700;color:var(--red)}
.nav{left:620px;top:46px;display:flex;gap:38px;font-size:14px;font-weight:500;color:#222}
.nav .active{color:var(--red)}
.nav-icons{left:968px;top:40px;display:flex;gap:8px}
.nav-icons span{width:30px;height:30px;border-radius:50%;display:block}
/* dropdown */
.dropdown{left:553px;top:125px;width:540px;height:165px;background:#fff;box-shadow:0 4px 14px rgba(0,0,0,.15);z-index:3;display:flex;padding:38px 0 0 32px}
.dropdown ul{list-style:none;width:170px;font-size:15px;line-height:30px;color:#333}
.dropdown li::before{content:"•";color:var(--red);margin-right:8px}
.dropdown .caret{left:162px;top:-10px;width:0;height:0;border:10px solid transparent;border-top:0;border-bottom-color:var(--red)}
/* hero */
.hero{left:0;top:125px;width:1200px;height:510px;background:linear-gradient(110deg,#4a2e24 0%,#b9b3ad 30%,#6d5a50 55%,#c6691f 70%,#3a2a24 100%)}
.hero-title{left:752px;top:310px;width:448px;height:60px;background:var(--red);color:#fff;font-size:32px;font-weight:700;padding:12px 22px;letter-spacing:1px}
.hero-sub{left:752px;top:372px;width:448px;height:42px;background:var(--yellow);color:#222;font-size:18px;padding:10px 24px}
.hero-dots{left:515px;top:603px;display:flex;gap:8px}
.hero-dots span{width:42px;height:4px;background:rgba(255,255,255,.6)}
/* headings */
.section-title{width:1200px;text-align:center;font-size:37px;font-weight:500;color:#111}
/* products */
.card{width:284px;height:293px;background:var(--gray);border:1px solid var(--line);text-align:center;padding-top:30px}
.card svg{display:block;margin:0 auto}
.card h3{font-size:19px;font-weight:700;margin:14px 0 20px}
.card p{font-size:12px;line-height:21px;color:var(--muted);padding:0 34px}
.card .go{width:28px;height:28px;border-radius:50%;background:var(--green);margin:16px auto 0;display:flex;align-items:center;justify-content:center}
.card .go.hot{background:linear-gradient(135deg,var(--yellow),var(--red))}
/* books */
.books{left:0;top:1410px;width:1200px;height:685px}
.book{width:208px;height:297px;background:#fff;border-radius:4px;text-align:center}
.book .cover{width:96px;height:140px;margin:22px auto 0}
.book h4{font-size:15px;font-weight:400;margin-top:28px;color:#333}
.book .price{font-size:18px;font-weight:700;margin-top:6px}
.book .buy{display:inline-block;margin-top:12px;background:var(--red);color:#fff;font-size:12px;font-weight:700;padding:6px 18px;border-radius:14px}
/* about */
.about-title{left:160px;top:2110px;font-size:37px;font-weight:500}
.about-sub{left:160px;top:2196px;font-size:21px;color:var(--red)}
.about-text{left:160px;top:2237px;width:283px;font-size:12px;line-height:20px;color:#333}
.about-text p+p{margin-top:16px}
.about-photo{left:453px;top:2200px;width:310px;height:245px;background:linear-gradient(135deg,#9aa4b2,#5b6670 50%,#8b4a3c);border:3px solid var(--red)}
.about-box{left:773px;top:2200px;width:262px;height:245px;border:2px solid var(--green);padding:26px 24px;font-size:12px;line-height:20px;color:#333}
.about-box p+p{margin-top:16px}
/* services */
.services{left:0;top:2570px;width:1200px;height:460px;background:linear-gradient(180deg,#ececec,#f7f7f7 50%,#e6e6e6)}
.svc{width:140px;text-align:center}
.svc .circle{width:140px;height:140px;border-radius:50%;display:flex;align-items:center;justify-content:center}
.svc .label{font-size:16px;font-weight:700;margin-top:22px;color:#111}
/* cta */
.cta{left:0;top:3030px;width:1200px;height:295px;background:var(--green);color:#fff;text-align:center}
.cta h2{font-size:36px;font-weight:500;margin-top:68px}
.cta p{font-size:12px;line-height:22px;margin:22px auto 0;width:640px}
.cta .btn{display:inline-block;margin-top:26px;background:var(--yellow);color:#111;font-size:14px;font-weight:700;padding:11px 32px;border-radius:22px}
/* footer */
.footer{left:0;top:3325px;width:1200px;height:341px;background:linear-gradient(100deg,#f5f3f6,#fff 40%,#f3eef5 70%,#eae0f0);border-top:6px solid var(--red)}
.footer::before{content:"";position:absolute;left:0;top:0;width:1200px;height:3px;background:var(--yellow)}
.f-brand{left:170px;top:80px;width:160px;text-align:center}
.f-brand .mark{width:70px;height:70px;background:var(--red);margin:0 auto 14px}
.f-brand .name{font-size:18px;font-weight:700;color:var(--red)}
.f-col{top:75px;font-size:12px;line-height:25px;color:#333}
.f-col h5{font-size:13px;font-weight:500;letter-spacing:1px;color:#222;margin-bottom:12px}
.socials{display:flex;gap:12px;align-items:center;margin:4px 0 18px}
.socials span{width:20px;height:20px;border-radius:50%;background:#111;display:block}
.copyright{left:0;top:3624px;width:1200px;text-align:center;font-size:11px;color:#333}
</style>
</head>
<body>

<div class="abs topbar">
  <div class="abs lang"><span></span><span></span></div>
  <div class="abs contact"><span>☎ Tel: 555 0142</span><span>✉ verk@vindaborgprent.is</span><span>◷ Mon - Fri: 9-17</span></div>
</div>

<header class="abs header">
  <div class="abs brand"><span class="mark"></span><span class="name">VINDABORGPRENT</span></div>
  <nav class="abs nav"><span class="active">Home</span><span>Services</span><span>Job submit</span><span>About Us</span></nav>
  <div class="abs nav-icons"><span style="background:var(--yellow)"></span><span style="background:var(--green)"></span></div>
</header>

<div class="abs dropdown">
  <div class="abs caret"></div>
  <ul><li>Essays</li><li>Business cards</li><li>Leaflets</li></ul>
  <ul><li>Bookprinting</li><li>Posters</li><li>Textbooks</li></ul>
  <ul><li>Brochure Printing</li><li>Calander 2018</li></ul>
</div>

<section class="abs hero" role="img" aria-label="Two print shop staff checking printed sheets beside a printing machine"></section>
<div class="abs hero-title">VINDABORGPRENT</div>
<div class="abs hero-sub">Lorem ipsum dolor sit amet, consectetur</div>
<div class="abs hero-dots"><span></span><span></span><span></span></div>

<h2 class="abs section-title" style="top:682px">Our Products</h2>

<div class="abs card" style="left:160px;top:760px">
  <svg width="60" height="70" viewBox="0 0 60 70" fill="none" stroke="var(--red)" stroke-width="2.5"><rect x="8" y="6" width="44" height="58" rx="4"/><path d="M16 20h28M16 30h28M16 40h18"/><circle cx="40" cy="50" r="7"/></svg>
  <h3>Essays</h3><p>Lorem ipsum dolor sit amet, consectet ur adipiscing elit, sed do eiusmod temod idunt ut labore et dolore magna.</p>
  <div class="go hot"><svg width="10" height="10" viewBox="0 0 10 10"><path d="M3 1l4 4-4 4" stroke="#fff" stroke-width="2" fill="none"/></svg></div>
</div>
<div class="abs card" style="left:458px;top:760px">
  <svg width="60" height="70" viewBox="0 0 60 70" fill="none" stroke="var(--red)" stroke-width="2.5"><rect x="12" y="10" width="36" height="54" rx="4"/><rect x="24" y="3" width="12" height="10"/><circle cx="30" cy="32" r="8"/><path d="M20 52h20"/></svg>
  <h3>Business cards</h3><p>Lorem ipsum dolor sit amet, consectet ur adipiscing elit, sed do eiusmod temod idunt ut labore et dolore magna.</p>
  <div class="go"><svg width="10" height="10" viewBox="0 0 10 10"><path d="M3 1l4 4-4 4" stroke="#fff" stroke-width="2" fill="none"/></svg></div>
</div>
<div class="abs card" style="left:755px;top:760px">
  <svg width="60" height="70" viewBox="0 0 60 70" fill="none" stroke="var(--red)" stroke-width="2.5"><rect x="8" y="4" width="34" height="50"/><rect x="18" y="14" width="34" height="52" fill="#f4f4f4"/><path d="M24 28h22M24 38h22M24 48h14"/></svg>
  <h3>Leaflets</h3><p>Lorem ipsum dolor sit amet, consectet ur adipiscing elit, sed do eiusmod temod idunt ut labore et dolore magna.</p>
  <div class="go"><svg width="10" height="10" viewBox="0 0 10 10"><path d="M3 1l4 4-4 4" stroke="#fff" stroke-width="2" fill="none"/></svg></div>
</div>
<div class="abs card" style="left:160px;top:1068px">
  <svg width="60" height="70" viewBox="0 0 60 70" fill="none" stroke="var(--red)" stroke-width="2.5"><rect x="10" y="4" width="40" height="60" rx="3"/><path d="M18 4v60M30 4v18l5-4 5 4V4"/></svg>
  <h3>Bookprinting</h3><p>Lorem ipsum dolor sit amet, consectet ur adipiscing elit, sed do eiusmod temod idunt ut labore et dolore magna.</p>
  <div class="go"><svg width="10" height="10" viewBox="0 0 10 10"><path d="M3 1l4 4-4 4" stroke="#fff" stroke-width="2" fill="none"/></svg></div>
</div>
<div class="abs card" style="left:458px;top:1068px">
  <svg width="60" height="70" viewBox="0 0 60 70" fill="none" stroke="var(--red)" stroke-width="2.5"><rect x="8" y="6" width="44" height="40"/><path d="M16 16h14v12H16zM36 18h10M36 26h10M16 36h30M22 46l-8 20M38 46l8 20M30 46v20"/></svg>
  <h3>Posters</h3><p>Lorem ipsum dolor sit amet, consectet ur adipiscing elit, sed do eiusmod temod idunt ut labore et dolore magna.</p>
  <div class="go"><svg width="10" height="10" viewBox="0 0 10 10"><path d="M3 1l4 4-4 4" stroke="#fff" stroke-width="2" fill="none"/></svg></div>
</div>
<div class="abs card" style="left:755px;top:1068px">
  <svg width="60" height="70" viewBox="0 0 60 70" fill="none" stroke="var(--red)" stroke-width="2.5"><rect x="6" y="8" width="48" height="18" rx="3"/><rect x="6" y="26" width="48" height="18" rx="3"/><rect x="6" y="44" width="48" height="18" rx="3"/><path d="M16 17h28M16 35h28M16 53h28"/></svg>
  <h3>Textbooks</h3><p>Lorem ipsum dolor sit amet, consectet ur adipiscing elit, sed do eiusmod temod idunt ut labore et dolore magna.</p>
  <div class="go"><svg width="10" height="10" viewBox="0 0 10 10"><path d="M3 1l4 4-4 4" stroke="#fff" stroke-width="2" fill="none"/></svg></div>
</div>

<section class="abs books">
  <svg class="abs" style="left:0;top:0" width="1200" height="685" viewBox="0 0 1200 685">
    <defs><linearGradient id="wave" x1="0" y1="0" x2="1" y2="0.3"><stop offset="0" stop-color="#f7c81b"/><stop offset=".35" stop-color="#f08a1c"/><stop offset=".7" stop-color="#e5361e"/><stop offset="1" stop-color="#d9141e"/></linearGradient></defs>
    <path d="M0 175 C 380 150, 820 90, 1200 8 L1200 540 C 820 560, 420 700, 0 680 Z" fill="url(#wave)"/>
  </svg>
  <h2 class="abs section-title" style="top:128px;color:#fff">Our Books</h2>
  <svg class="abs" style="left:108px;top:362px" width="18" height="28" viewBox="0 0 18 28"><path d="M14 2L4 14l10 12" stroke="#fff" stroke-width="3" fill="none"/></svg>
  <svg class="abs" style="left:1075px;top:362px" width="18" height="28" viewBox="0 0 18 28"><path d="M4 2l10 12L4 26" stroke="#fff" stroke-width="3" fill="none"/></svg>
  <div class="abs book" style="left:162px;top:203px"><div class="cover" role="img" aria-label="Book cover: Story of Thought" style="background:linear-gradient(90deg,#ddd,#fff 40%,#eee)"></div><h4>Story of Thought</h4><div class="price">4.900 kr</div><span class="buy">Buy Now</span></div>
  <div class="abs book" style="left:385px;top:203px"><div class="cover" role="img" aria-label="Book cover: Systems Design" style="background:linear-gradient(90deg,#ccc,#f5f5f5 40%,#9aa59a)"></div><h4>Systems Design</h4><div class="price">5.900 kr</div><span class="buy">Buy Now</span></div>
  <div class="abs book" style="left:608px;top:203px"><div class="cover" role="img" aria-label="Book cover: Clear Writing" style="background:linear-gradient(135deg,#8a6a22,#c9a442 60%,#6b4f18)"></div><h4>Clear Writing</h4><div class="price">5.450 kr</div><span class="buy">Buy Now</span></div>
  <div class="abs book" style="left:831px;top:203px"><div class="cover" role="img" aria-label="Book cover: Tölur frá Byrjun" style="background:linear-gradient(135deg,#e8c7d8,#f7f0f4 50%,#d64b8a)"></div><h4>Tölur frá Byrjun</h4><div class="price">5.990 kr</div><span class="buy">Buy Now</span></div>
</section>

<h2 class="abs about-title">About Us</h2>
<div class="abs about-sub">Welcome to University</div>
<div class="abs about-text">
  <p>University education is a company located in the campus, which has specialized in the service of school staff, as well as providing general public printing.</p>
  <p>Higher education publishes seminars and first-class textbooks for courses, prints theses for lesson, as well as working on an unprecedented number of smaller pieces for students, teachers and organizations. These include brochures, reports, questionnaires, business cards, books, OCR scanning and more.</p>
</div>
<div class="abs about-photo" role="img" aria-label="Two staff members working together at a large office printer"></div>
<div class="abs about-box">
  <p>Higher education is a tailored print shop. The Leaf is the official eco-label of the Nordic countries, which has created a foothold in this country and is known among consumers.</p>
  <p>University education is located at the corner of Hrafnagata and Norðurgata, (walked into Norðurgata)</p>
</div>

<section class="abs services" role="img" aria-label="Desk scene seen from above with coffee cups, papers and hands at work">
  <div class="abs svc" style="left:377px;top:125px">
    <div class="circle" style="background:var(--red)"><svg width="70" height="60" viewBox="0 0 70 60" fill="none" stroke="#fff" stroke-width="2.5"><path d="M4 28L66 4 50 56 32 38zM66 4L32 38v16l8-10"/></svg></div>
    <div class="label">SENDA VERK</div>
  </div>
  <div class="abs svc" style="left:530px;top:125px">
    <div class="circle" style="background:var(--yellow)"><svg width="64" height="60" viewBox="0 0 64 60" fill="none" stroke="#222" stroke-width="2.5"><path d="M32 4C14 4 4 16 4 30s12 26 26 26c6 0 6-6 2-10-3-4 0-8 5-8h9c10 0 14-6 14-12C60 14 48 4 32 4z"/><circle cx="18" cy="24" r="4"/><circle cx="30" cy="15" r="4"/><circle cx="44" cy="20" r="4"/></svg></div>
    <div class="label">HANNA VERK</div>
  </div>
  <div class="abs svc" style="left:687px;top:125px">
    <div class="circle" style="background:var(--green)"><svg width="64" height="64" viewBox="0 0 64 64" fill="none" stroke="#fff" stroke-width="2.5"><path d="M10 56L10 8h12v48zM22 52L34 14l11 4-12 38zM26 56l26-30 8 7-24 23z"/><circle cx="16" cy="48" r="2"/></svg></div>
    <div class="label">FA TILBOD</div>
  </div>
</section>

<section class="abs cta">
  <h2>Get Started!</h2>
  <p>Sed ut perspiciatis unde omnis iste natus error sit voluptatem accusantium doloremque laudantium, totam reaperied ut perspiciatis unde omnis iste natus error sit voluptatem accusantium doloremque laudantium, totam rem aper</p>
  <span class="btn">CONTACT US</span>
</section>

<footer class="abs footer">
  <div class="abs f-brand"><div class="mark"></div><div class="name">VINDABORGPRENT</div></div>
  <div class="abs f-col" style="left:415px"><h5>COMPANY</h5>Sed uerspiciatism<br>Comnisteatusit<br>Sed uerspiciatism<br>Comnisteatusit<br>Perspiciatis unde</div>
  <div class="abs f-col" style="left:563px"><h5>LINKS</h5>Sed uerspiciatism<br>Comnisteatusit<br>Sed uerspiciatism<br>Comnisteatusit<br>Perspiciatis unde</div>
  <div class="abs f-col" style="left:720px"><h5>CONNECT</h5>
    <div class="socials"><svg width="24" height="18" viewBox="0 0 24 18"><rect x="1" y="1" width="22" height="16" fill="none" stroke="#111" stroke-width="2"/><path d="M1 1l11 9 11-9" fill="none" stroke="#111" stroke-width="2"/></svg><span></span><span></span><span></span></div>
    <h5>POLICIES</h5>Privacy<br>Complaint and Feedback</div>
  <div class="abs f-col" style="left:927px"><h5>OTHER LINKS</h5>Sed uterspiciatis<br>Sed uerspiciatism<br>Comnisteatusit<br>Perspiciatis unde<br>Sed uerspiciatism</div>
</footer>
<div class="abs copyright">© 2018 All Rights are Reserved. Privacy Policy | Terms of Use | Contact</div>

</body>
</html>
```